RTO Carts Website

Our business is a golf cart rental and repair business. We live on a bridgeless barrier Island so there are no cars... golf carts are the main mode of transportation. We need a website that:
1. Reflects the island attitude.
2. Gives our contact information and hours of operation and rates.
3. Allows a page to show carts for sale.
4. Allows a downloadable liability form.
5. Allows for Reservations. A calendar plus a waiting list for a waiting list.
6. Allows payments through fund dock or credit card.

```html
<!DOCTYPE html>
<html lang="en">
<head>
<meta charset="utf-8">
<title>RTO Carts – Golf Cart Rental and Repair</title>
<link href="https://fonts.googleapis.com/css2?family=Open+Sans:wght@400;600;700&display=swap" rel="stylesheet">
<style>
:root{
  --nav-dark:#2a1d19;
  --accent-yellow:#f2c200;
  --orange:#f39c1f;
  --sale-red:#e0413d;
  --green-btn:#1a7f3a;
  --blue-btn:#2f8fd0;
  --link-blue:#1f86b5;
  --bar-dark:#3a3f44;
  --footer-dark:#3b3b3b;
  --text:#333;
  --muted:#555;
  --card-bg:#fafafa;
  --line:#e3e3e3;
}
*{box-sizing:border-box;margin:0;padding:0}
html,body{width:810px;height:1200px;overflow:hidden}
body{
  position:relative;font-family:"Open Sans",Arial,sans-serif;color:var(--text);
  background:linear-gradient(180deg,#bcd7ea 0,#e9f1f6 120px,#dfe9e6 230px,#a9c78a 300px,#cfe0b8 400px,#fff 480px,#fff 100%);
}
.abs{position:absolute}
.brand{left:115px;top:28px;display:flex;align-items:center;gap:8px}
.brand-dot{width:38px;height:38px;border-radius:50%;background:#1f86b5}
.brand-name{font-size:26px;font-weight:700;color:#222;letter-spacing:-.5px}
.top-info{left:500px;top:14px;font-size:8px;color:#444;line-height:1}
.top-info li{list-style:none;display:flex;align-items:center;gap:8px;height:19px;white-space:nowrap}
.top-info svg{width:10px;height:10px}
.rating{font-size:7px}
.rating b{color:#2f8fd0;font-size:10px;font-weight:600}
.rating .stars{color:#2f8fd0;font-size:9px;letter-spacing:1px}
.nav{left:116px;top:101px;width:579px;height:34px;background:var(--nav-dark);display:flex;align-items:center}
.nav a{color:#fff;font-size:8px;text-decoration:none;font-weight:600;padding:0 16px;line-height:34px}
.nav a.active{background:var(--accent-yellow);padding:0 13px}
.nav .social{margin-left:auto;display:flex;gap:6px;padding-right:14px}
.nav .social span{width:13px;height:13px;border-radius:50%;background:#fff}
.slider{left:116px;top:146px;width:579px;height:262px;background:#fff;box-shadow:0 0 4px rgba(0,0,0,.15)}
.slider h1{position:absolute;left:32px;top:32px;font-size:28px;font-weight:600;color:var(--orange)}
.slider p{position:absolute;left:34px;top:80px;width:245px;font-size:6.5px;line-height:13.5px;color:var(--muted);text-align:justify}
.slider .deal{position:absolute;left:34px;top:143px;font-size:20px;color:var(--sale-red)}
.btn{position:absolute;color:#fff;font-size:8px;display:flex;align-items:center;justify-content:center;border-radius:2px}
.shop{left:34px;top:184px;width:62px;height:26px;background:var(--green-btn)}
.dots{position:absolute;left:114px;top:194px;display:flex;gap:5px}
.dots span{width:7px;height:7px;border-radius:50%;background:#333;border:1.5px solid #ddd}
.dots span:first-child{background:#d33}
.slide-photo{position:absolute;left:290px;top:28px;width:270px;height:205px;background:radial-gradient(ellipse at center,#b83030 0,#5a2a2a 35%,#e8eef3 70%,#fff 100%)}
.arrow{width:26px;height:26px;border-radius:50%;background:#fff;box-shadow:0 0 5px rgba(0,0,0,.35);display:flex;align-items:center;justify-content:center}
.res-bar{left:116px;top:408px;width:579px;height:51px;background:var(--bar-dark);display:flex;align-items:center;padding:0 12px}
.res-bar h2{color:#fff;font-size:14px;font-weight:400;width:122px}
.res-bar h2 small{font-size:10px}
.res-bar .field{width:110px;height:24px;background:#fff;margin-right:12px;font-size:6.5px;color:#666;padding:9px 12px}
.res-bar .go{width:72px;height:24px;background:var(--blue-btn);color:#fff;font-size:10px;display:flex;align-items:center;justify-content:center}
.welcome-photo{left:116px;top:487px;width:185px;height:147px;border:3px solid #fff;box-shadow:0 0 3px rgba(0,0,0,.25);background:linear-gradient(180deg,#3d6fa8 0,#dfe8f2 40%,#7b7564 62%,#3d7f80 75%,#2b5e5b 100%)}
.welcome{left:328px;top:484px;width:370px}
.welcome h2{font-size:14px;font-weight:400;color:#222}
.welcome h2 span{color:var(--link-blue);font-weight:600}
.welcome p{font-family:Arial,sans-serif;font-size:6.5px;line-height:12.8px;color:var(--muted);margin-top:6px}
.more{left:326px;top:608px;width:58px;height:26px;background:#2b2b2b}
.products-title{left:116px;top:650px;font-size:14px;font-weight:400;color:#333}
.rule{left:116px;top:681px;width:579px;height:1px;background:var(--line)}
.card{top:697px;width:137px;height:222px;background:var(--card-bg);border:1px solid #ececec}
.card .pic{height:124px;background:#fff;border-bottom:1px solid #eee;display:flex;align-items:center;justify-content:center}
.card .pic div{width:110px;height:100px}
.card h3{font-size:9px;font-weight:400;margin:14px 0 0 12px;color:#222}
.card p{font-size:6.5px;line-height:12.5px;color:var(--muted);margin:6px 10px 0 12px}
.card .price{font-size:10px;font-weight:600;margin:10px 0 0 16px;color:#111}
.banner{left:116px;top:943px;width:579px;height:145px;border:1px solid #ddd;background:linear-gradient(180deg,#9fbb62 0,#dfe8cc 30%,#f5f6f1 60%,#fff 100%)}
.banner .copy{position:absolute;left:74px;top:22px;text-align:center;color:#222;font-size:24px;line-height:32px;font-weight:600}
.banner .copy .lead{font-weight:400;font-size:22px}
.banner .copy b{font-weight:700;font-size:27px}
.banner .copy .tail{font-weight:400;font-size:21px}
.banner .cart{position:absolute;left:375px;top:10px;width:170px;height:128px;background:radial-gradient(ellipse at center,#b83030 0,#3a2a2a 45%,rgba(255,255,255,0) 72%)}
.footer{left:0;top:1111px;width:810px;height:89px;background:var(--footer-dark);border-top:3px solid var(--link-blue)}
.footer nav{position:absolute;left:117px;top:21px;font-size:7px;color:#eee}
.footer nav span{margin:0 5px}
.footer .copy{position:absolute;left:116px;top:43px;font-size:7px;color:#ccc}
.pay{position:absolute;left:458px;top:36px;display:flex;gap:4px}
.pay span{width:26px;height:13px;background:#d9822b;font-size:4.5px;color:#fff;display:flex;align-items:center;justify-content:center;white-space:nowrap}
.pay span:nth-child(2){background:#2a6fb8}.pay span:nth-child(3){background:#c8c8c8;color:#333}.pay span:nth-child(4){background:#2a8fd0}
.soc{position:absolute;left:592px;top:30px;display:flex;gap:8px}
.soc span{width:19px;height:19px;border-radius:50%}
</style>
</head>
<body>
<div class="abs brand"><span class="brand-dot"></span><span class="brand-name">RTO Carts</span></div>

<ul class="abs top-info">
  <li><svg viewBox="0 0 10 10"><path d="M1 1h4l4 4-4 4-4-4z" fill="#555"/></svg>Rental Shop · Repair Service · ATVs &amp; Golf Carts</li>
  <li><svg viewBox="0 0 10 10"><path d="M5 0a3.5 3.5 0 0 1 3.5 3.5C8.5 6 5 10 5 10S1.5 6 1.5 3.5A3.5 3.5 0 0 1 5 0z" fill="#333"/><circle cx="5" cy="3.5" r="1.3" fill="#fff"/></svg>214 Palm Shore Rd., Gulf Key, Florida 30000</li>
  <li><svg viewBox="0 0 10 10"><path d="M1 3q4-3 8 0v1.5H7V3.6H3v.9H1z M2 5h6v4H2z" fill="#222"/></svg>+1 555-010-4477</li>
  <li class="rating"><b>5.0</b><span class="stars">★★★★★</span>(7 ratings)</li>
</ul>

<nav class="abs nav">
  <a class="active">HOME</a><a>ABOUT US</a><a>RENTAL AND REPAIR</a><a>SERVICES</a><a>BLOG</a><a>CONTACT US</a>
  <div class="social"><span></span><span></span><span></span><span></span></div>
</nav>

<div class="abs arrow" style="left:35px;top:289px"><svg width="8" height="8" viewBox="0 0 8 8"><path d="M5 1 2 4l3 3" stroke="#666" fill="none" stroke-width="1.5"/></svg></div>
<div class="abs arrow" style="left:754px;top:289px"><svg width="8" height="8" viewBox="0 0 8 8"><path d="M3 1l3 3-3 3" stroke="#666" fill="none" stroke-width="1.5"/></svg></div>

<section class="abs slider">
  <h1>Golf Cart Rental</h1>
  <p>Masagni dolores eoquie voluptate msequi nesciunt. Nique porro quisquam est qui dolorem ipsumquia dolor sitamet consectet, adipisci unumquam eius.Masagni dolores eoquie voluptate msequi nesciunt. Nique porro quisquam est qui dolorem ipsumquia dolor sitamet consectet,</p>
  <div class="deal">40 % OFF</div>
  <div class="btn shop">SHOP NOW</div>
  <div class="dots"><span></span><span></span><span></span><span></span></div>
  <div class="slide-photo" role="img" aria-label="Red utility golf cart with black roll cage"></div>
</section>

<form class="abs res-bar">
  <h2>Reservation <small>Form</small></h2>
  <div class="field">Cart type</div><div class="field">Phone no</div><div class="field">Location</div>
  <div class="go">Reservation</div>
</form>

<div class="abs welcome-photo" role="img" aria-label="Island beach houses under a cloudy sky by the sea"></div>
<div class="abs welcome">
  <h2>Welcome To <span>RTO Carts</span></h2>
  <p>Etiam quis mi ante. Donec iaculis ornare enim non dapibus. Vivamus ac nisi eros. Nam non commodo mi. Pellentesque habitant morbi tristique senectus et netus et malesuada fames ac turpis egestas.Etiam quis mi ante. Donec iaculis ornare enim non dapibus. Vivamus ac nisi eros. Nam non commodo mi. Pellentesque habitant morbi tristique senectus et netus et malesuada fames ac turpis egestas.</p>
  <p>Etiam quis mi ante. Donec iaculis ornare enim non dapibus. Vivamus ac nisi eros. Nam non commodo mi. Pellentesque habitant morbi tristique senectus et netus et malesuada fames ac turpis egestas.</p>
</div>
<div class="abs btn more">Read More</div>

<h2 class="abs products-title">Our Products</h2>
<div class="abs rule"></div>

<article class="abs card" style="left:116px"><div class="pic"><div role="img" aria-label="Red golf cart with canopy" style="background:radial-gradient(ellipse,#a52b2b 0,#fff 70%)"></div></div><h3>Eget elementum vel</h3><p>Masagni dolores eoquie voluptate msequi nesciunt. Nique .</p><div class="price">$299.99</div></article>
<article class="abs card" style="left:263px"><div class="pic"><div role="img" aria-label="Silver quad ATV" style="background:radial-gradient(ellipse,#666 0,#fff 70%)"></div></div><h3>Mes cuml dia sed in lacus</h3><p>Masagni dolores eoquie voluptate msequi nesciunt. Nique .</p><div class="price">$299.99</div></article>
<article class="abs card" style="left:411px"><div class="pic"><div role="img" aria-label="Green utility cart" style="background:radial-gradient(ellipse,#1f5a3a 0,#fff 70%)"></div></div><h3>Lorem ipsum dolor sit</h3><p>Masagni dolores eoquie voluptate msequi nesciunt. Nique .</p><div class="price">$299.99</div></article>
<article class="abs card" style="left:558px"><div class="pic"><div role="img" aria-label="White golf cart with canopy" style="background:radial-gradient(ellipse,#bfb6a4 0,#fff 70%)"></div></div><h3>Vivamus vel eros eget</h3><p>Masagni dolores eoquie voluptate msequi nesciunt. Nique .</p><div class="price">$299.99</div></article>

<section class="abs banner" role="img" aria-label="Golf course green with a red utility cart">
  <div class="copy"><span class="lead">We do </span><b>golf cart</b><br>Rental and Repair<br><span class="tail">business</span></div>
  <div class="cart"></div>
</section>

<footer class="abs footer">
  <nav>Home <span>|</span> About <span>|</span> Rental and Repair <span>|</span> Blog <span>|</span> Contact</nav>
  <div class="copy">©2014 RTO Carts, All Rights Reserved.</div>
  <div class="pay"><span>fund dock</span><span>Korvo</span><span>Tessel</span><span>Nimbo</span></div>
  <div class="soc"><span style="background:#3aa3d8"></span><span style="background:#2f5fa8"></span><span style="background:#666"></span><span style="background:#e25a8d"></span></div>
</footer>
</body>
</html>
```